Problem Solving Guide- PDF Template

We are looking for an editable PDF template design for our Epoxy Floor Coatings Problem Solving Guide.

Target Market(s)

This guide will be on our website and we will also email it to customers

Industry/Entity Type

Online Shopping

Colors
f78f20
ffffff
5c5c5c
000000

Requirements
Must have
• We are looking for a very modern and clean design. Each page of the guide will address a different issue. There will be 20-25 pages in total for the completed guide, however we just need a template that we can use to create each page so that they look the same. Each page must have our logo, a spot to add a photo of the issue being discussed. Then each page will have the following sections: DESCRIPTION,CAUSE,REPAIR,PREVENTION. At the bottom of each page we would like to direct people to our website for more information. I am attaching the current guide that we have. This shows the basic information that each page will have but as you can see it is old, outdated and anything but modern. As part of the design you can put the different parts of information in circles, squares, use arrows etc. to make it appealing. I am also attaching a copy of our color chart that appears on our website to give you an idea of some of the other graphic designs that we use. Our colors are Orange (please use the same orange as in our logo) grey, black and white. Our website is www.resinmarket.net. There is also a picture of "bubbles in epoxy"-this is an example of a picture we will show to address one issue.

```html
<!DOCTYPE html>
<html lang="en">
<head>
<meta charset="utf-8">
<title>Problem Solving Guide – Bubbles in Epoxy</title>
<link rel="stylesheet" href="https://fonts.googleapis.com/css2?family=Open+Sans:wght@400;600;700&family=Roboto+Condensed:wght@700&display=swap">
<style>
  :root {
    --orange: #f26722;
    --grey-text: #5c5c5c;
    --grey-footer: #737578;
    --tab-grey: #e6e7e8;
    --backdrop: #d1d2d4;
    --white: #ffffff;
  }
  * { margin: 0; padding: 0; box-sizing: border-box; }
  html, body { width: 1047px; height: 1200px; overflow: hidden; }
  body {
    background: var(--backdrop);
    font-family: "Open Sans", sans-serif;
    color: var(--grey-text);
    position: relative;
  }
  .page {
    position: absolute; left: 110px; top: 120px; width: 765px; height: 990px;
    background: var(--white);
    box-shadow: 6px 6px 8px rgba(0,0,0,0.35);
    overflow: hidden;
  }
  .brand { position: absolute; left: 21px; top: 24px; display: flex; align-items: center; gap: 14px; }
  .brand-dot { width: 68px; height: 68px; border-radius: 50%; background: var(--orange); }
  .brand-name { font-size: 36px; font-weight: 600; color: var(--orange); line-height: 1; letter-spacing: -0.5px; }
  .brand-tagline { font-size: 11px; font-weight: 600; color: var(--grey-text); margin-top: 4px; }
  .title-banner {
    position: absolute; left: 394px; top: 34px; width: 371px; height: 49px;
    background: var(--orange);
    clip-path: polygon(14px 0, 100% 0, 100% 100%, 0 100%);
    color: var(--white); font-weight: 700; font-size: 23px;
    display: flex; align-items: center; justify-content: flex-end; padding-right: 32px;
  }
  .issue-photo {
    position: absolute; left: 0; top: 101px; width: 765px; height: 301px;
    background: linear-gradient(160deg, #8b8983 0%, #9f9d96 55%, #aaa8a2 100%);
  }
  .room-photo {
    position: absolute; left: 537px; top: 305px; width: 194px; height: 194px;
    border-radius: 50%; background: var(--orange); padding: 10px;
  }
  .room-photo-inner {
    width: 100%; height: 100%; border-radius: 50%; border: 2px solid var(--white);
    background: linear-gradient(180deg, #2e3133 0%, #6d7173 45%, #d9dcdc 70%, #eef0ef 100%);
  }
  .section-tab {
    position: absolute; left: 0; width: 140px; height: 29px;
    background: var(--tab-grey);
    clip-path: polygon(0 0, 130px 0, 140px 50%, 130px 100%, 0 100%);
    color: var(--orange); font-weight: 700; font-size: 15.5px;
    padding-left: 24px; line-height: 29px;
  }
  .body-text {
    position: absolute; left: 24px; width: 712px;
    font-size: 14px; line-height: 20px; text-align: justify; letter-spacing: -0.3px;
  }
  .footer { position: absolute; left: 0; top: 940px; width: 765px; height: 50px; }
  .footer-bar { position: absolute; inset: 0; background: var(--grey-footer); }
  .footer-phone {
    position: absolute; left: 0; top: 0; width: 295px; height: 50px;
    background: var(--orange);
    clip-path: polygon(0 0, 100% 0, calc(100% - 17px) 100%, 0 100%);
  }
  .footer-phone-edge {
    position: absolute; left: 0; top: 0; width: 301px; height: 50px; background: var(--white);
    clip-path: polygon(295px 0, 301px 0, 284px 100%, 278px 100%);
  }
  .phone-number {
    position: absolute; left: 64px; top: 8px;
    font-family: "Roboto Condensed", sans-serif; font-weight: 700; font-size: 28px; color: var(--white);
  }
  .phone-icon { position: absolute; left: 24px; top: 11px; }
  .footer-web {
    position: absolute; left: 302px; top: 17px; color: var(--white);
    font-size: 10px; display: flex; align-items: center; gap: 4px;
  }
  .footer-web strong { font-size: 14px; font-weight: 600; }
</style>
</head>
<body>
  <main class="page">
    <header>
      <div class="brand">
        <div class="brand-dot"></div>
        <div>
          <div class="brand-name">resinmarket</div>
          <div class="brand-tagline">Floor coatings, supplies and know-how.</div>
        </div>
      </div>
      <div class="title-banner">BUBBLES IN EPOXY</div>
    </header>

    <div class="issue-photo" role="img" aria-label="Close-up photo of bubbles and blisters in a grey epoxy floor coating"></div>
    <div class="room-photo"><div class="room-photo-inner" role="img" aria-label="Photo of a modern kitchen with a glossy white epoxy floor"></div></div>

    <div class="section-tab" style="top:433px">DESCRIPTION</div>
    <p class="body-text" style="top:467px">Difference in color or shading of topcoat.</p>

    <div class="section-tab" style="top:514px">CAUSE</div>
    <p class="body-text" style="top:543px">Retouching after 15 minutes: Color float issues arise when a pgmented epoxy has been applied and is re&#8209;touch or rooled again after sitting for 15 minutes or longer. Different shadesin the color may result.</p>
    <p class="body-text" style="top:602px">Using different batch numberes: Coloring can vary from batch to batch. Different batches used on the same project can result in color variances.</p>

    <div class="section-tab" style="top:659px">REPAIR</div>
    <p class="body-text" style="top:690px">Back rool the entire area always using an 18”, woven, shed-resistant, 3/8” nap roller. Always try to go across the entire area from side&#8209;to&#8209;side.</p>
    <p class="body-text" style="top:748px">When possible, recoats should alweys be completed with the same coating batsch.</p>
    <p class="body-text" style="top:787px">If batches are different, blend colored (base) side first before adding activator.</p>

    <div class="section-tab" style="top:823px">PREVENTION</div>
    <p class="body-text" style="top:854px;text-align:left">If material needs to be re-touched or rolle for any reason, it needs to be done within 10 minutes of applica-<br>tion.</p>

    <footer class="footer">
      <div class="footer-bar"></div>
      <div class="footer-phone"></div>
      <div class="footer-phone-edge"></div>
      <svg class="phone-icon" width="30" height="28" viewBox="0 0 30 28" aria-hidden="true">
        <path d="M6 3 L10 3 L12 9 L9 11 Q11 17 16 20 L18 17 L24 19 L24 23 Q23 26 19 25 Q6 21 3 8 Q3 4 6 3 Z" fill="#fff"/>
        <path d="M16 4 Q22 5 23 11" stroke="#fff" stroke-width="2" fill="none"/>
        <path d="M16 0 Q26 1 27 11" stroke="#fff" stroke-width="2" fill="none"/>
      </svg>
      <div class="phone-number">1-888-555-0142</div>
      <div class="footer-web">
        <span>For additional information and application instructions visit-</span>
        <svg width="13" height="13" viewBox="0 0 13 13" aria-hidden="true">
          <circle cx="6.5" cy="6.5" r="5.5" stroke="#fff" fill="none"/>
          <ellipse cx="6.5" cy="6.5" rx="2.4" ry="5.5" stroke="#fff" fill="none"/>
          <path d="M1 6.5 H12" stroke="#fff"/>
        </svg>
        <strong>www.resinmarket.net</strong>
      </div>
    </footer>
  </main>
</body>
</html>
```